Tellwick Asset Management - Corporate Letter Head Project

Looking for a classy design based on our current logo. Please find current logo source file in files. With our color scheme.

Target Market(s)

We're an investment firm, the letterhead needs to look professional and attractive to clients.

Industry/Entity Type

Hedgefund

Colors
0054AA
0677BA
7BADD7
CADEEF
E8F1F8

Requirements
Must have
• Our logo, address, phone number, and email

```html
<!DOCTYPE html>
<html lang="en">
<head>
<meta charset="utf-8">
<title>Tellwick Asset Management – Letterhead</title>
<link rel="stylesheet" href="https://fonts.googleapis.com/css2?family=Montserrat:wght@800&family=Roboto:wght@400;500;700&display=swap">
<style>
  :root {
    --brand-deep: #0054AA;
    --brand-mid: #0677BA;
    --brand-soft: #7BADD7;
    --brand-pale: #CADEEF;
    --brand-mist: #E8F1F8;
    --grey: #8a8a8a;
    --ink: #111111;
    --paper: #ffffff;
  }
  * { margin: 0; padding: 0; box-sizing: border-box; }
  html, body { width: 848px; height: 1200px; overflow: hidden; background: var(--paper); }
  .letterhead {
    position: relative;
    width: 848px;
    height: 1200px;
    background: var(--paper);
    font-family: "Roboto", Arial, sans-serif;
    overflow: hidden;
  }
  .swoosh { position: absolute; left: 0; top: 0; width: 848px; height: 1200px; }
  .brand {
    position: absolute;
    left: 55px;
    top: 91px;
    display: flex;
    align-items: center;
    gap: 16px;
  }
  .brand-square {
    width: 76px;
    height: 76px;
    border: 2px solid var(--brand-deep);
    flex: none;
  }
  .brand-name {
    width: 260px;
    font-weight: 500;
    font-size: 28px;
    line-height: 1.15;
    color: var(--brand-deep);
    letter-spacing: 0.3px;
  }
  .sender {
    position: absolute;
    right: 45px;
    top: 86px;
    text-align: right;
  }
  .sender-name {
    display: inline-block;
    font-family: "Montserrat", Arial, sans-serif;
    font-weight: 800;
    font-size: 26px;
    line-height: 1;
    color: var(--brand-deep);
    position: relative;
    padding-bottom: 5px;
  }
  .sender-name::after {
    content: "";
    position: absolute;
    right: 0;
    bottom: 0;
    width: 89px;
    height: 2px;
    background: var(--brand-mid);
  }
  .sender-contact {
    font-size: 18px;
    line-height: 24px;
    color: var(--grey);
    margin-top: 6px;
  }
  .company-footer {
    position: absolute;
    left: 55px;
    top: 1090px;
  }
  .company-name {
    display: inline-block;
    font-weight: 700;
    font-size: 23px;
    line-height: 1.2;
    color: var(--brand-deep);
    position: relative;
    padding-bottom: 3px;
  }
  .company-name::after {
    content: "";
    position: absolute;
    left: 5px;
    bottom: 0;
    width: 142px;
    height: 1.5px;
    background: var(--brand-mid);
  }
  .company-address {
    font-size: 15px;
    line-height: 18px;
    color: var(--ink);
    margin-top: 4px;
  }
</style>
</head>
<body>
<div class="letterhead">
  <svg class="swoosh" viewBox="0 0 848 1200" aria-hidden="true">
    <path d="M0 0 H848 V20 C560 14 220 28 0 74 Z" fill="var(--brand-deep)"/>
    <path d="M418 29 C600 18 780 18 848 21 V67 C800 42 650 26 418 29 Z" fill="var(--brand-soft)"/>
    <path d="M402 1200 C620 1188 800 1160 848 1118 V1200 Z" fill="var(--brand-deep)"/>
    <path d="M598 1173 C700 1148 800 1105 848 1070 V1118 C800 1142 700 1160 598 1173 Z" fill="var(--brand-soft)"/>
  </svg>

  <header class="brand">
    <div class="brand-square"></div>
    <div class="brand-name">Tellwick Asset Management</div>
  </header>

  <section class="sender">
    <div class="sender-name">MARA LINDQVIST</div>
    <div class="sender-contact">
      <div class="sender-phone">123 456 7890</div>
      <div class="sender-email">info@example.com</div>
    </div>
  </section>

  <footer class="company-footer">
    <div class="company-name">Tellwick Asset Management</div>
    <div class="company-address">
      <div>123, Lorem Ipsum is simply dummy text</div>
      <div>City State Country</div>
    </div>
  </footer>
</div>
</body>
</html>
```